Quiet Please - Poster Design Comp

This contest is to design a poster for:

"Quiet Please Minds At Work"

Here is a poster I quickly designed as an example: [url removed, login to view]

Have FUN!!!

```html
<!DOCTYPE html>
<html lang="en">
<head>
<meta charset="utf-8">
<title>Quiet Please — Mind at work</title>
<link rel="stylesheet" href="https://fonts.googleapis.com/css2?family=Encode+Sans+Condensed:wght@400&family=Tinos&family=Ubuntu+Mono&display=swap">
<style>
  :root {
    --bg-left: #5700b8;
    --bg-mid: #40005e;
    --bg-right: #2c0018;
    --line-blue: #3b2fc8;
    --line-pink: #ff3fd0;
    --bar-top: #1a1060;
    --bar-base: #05020c;
    --accent-pink: #ff3aa8;
    --headline-rose: #d46aa6;
    --tagline-magenta: #ff3fe6;
    --serif-pink: #ff2fa0;
  }
  html, body {
    margin: 0;
    padding: 0;
    width: 900px;
    height: 1200px;
    overflow: hidden;
    background: var(--bar-base);
  }
  .poster {
    display: block;
    width: 900px;
    height: 1200px;
  }
  .headline {
    font-family: "Encode Sans Condensed", "Arial Narrow", sans-serif;
    font-size: 64px;
    fill: var(--headline-rose);
  }
  .tagline {
    font-family: "Ubuntu Mono", monospace;
    font-size: 68px;
    fill: var(--tagline-magenta);
  }
  .side-title {
    font-family: "Tinos", "Times New Roman", serif;
    font-size: 36px;
    fill: var(--serif-pink);
  }
  .sweep {
    fill: none;
    stroke: var(--accent-pink);
    stroke-width: 2;
  }
  .rule { stroke-width: 4; }
</style>
</head>
<body>
<svg class="poster" viewBox="0 0 900 1200" xmlns="http://www.w3.org/2000/svg">
  <defs>
    <linearGradient id="backdrop" x1="0" y1="0" x2="1" y2="0">
      <stop offset="0" stop-color="var(--bg-left)"/>
      <stop offset="0.55" stop-color="var(--bg-mid)"/>
      <stop offset="1" stop-color="var(--bg-right)"/>
    </linearGradient>
    <linearGradient id="rule-fade" x1="0" y1="0" x2="1" y2="0">
      <stop offset="0" stop-color="var(--line-blue)"/>
      <stop offset="1" stop-color="var(--line-pink)"/>
    </linearGradient>
    <linearGradient id="bar-down" x1="0" y1="0" x2="0" y2="1">
      <stop offset="0" stop-color="var(--bar-top)"/>
      <stop offset="1" stop-color="var(--bar-base)"/>
    </linearGradient>
    <linearGradient id="bar-up" x1="0" y1="1" x2="0" y2="0">
      <stop offset="0" stop-color="var(--bar-top)"/>
      <stop offset="1" stop-color="var(--bar-base)"/>
    </linearGradient>
    <linearGradient id="mouth-tone" x1="0" y1="0" x2="1" y2="1">
      <stop offset="0" stop-color="#e04fd0" stop-opacity="0.35"/>
      <stop offset="1" stop-color="#ff5ac8" stop-opacity="0.2"/>
    </linearGradient>
  </defs>

  <rect class="backdrop" width="900" height="1200" fill="url(#backdrop)"/>

  <!-- top and bottom rules -->
  <g class="rules" fill="url(#rule-fade)">
    <rect x="0" y="8" width="900" height="5"/>
    <rect x="0" y="26" width="900" height="5"/>
    <rect x="0" y="1148" width="900" height="5"/>
    <rect x="0" y="1176" width="900" height="5"/>
  </g>

  <!-- corner bar clusters -->
  <g class="bars-top-left" fill="url(#bar-down)">
    <rect x="8" y="0" width="20" height="403"/>
    <rect x="35" y="0" width="20" height="303"/>
    <rect x="67" y="0" width="18" height="230"/>
    <rect x="93" y="0" width="20" height="151"/>
    <rect x="120" y="0" width="18" height="88"/>
  </g>
  <g class="bars-top-right" fill="url(#bar-down)">
    <rect x="880" y="0" width="18" height="397"/>
    <rect x="851" y="0" width="20" height="298"/>
    <rect x="822" y="0" width="18" height="225"/>
    <rect x="795" y="0" width="18" height="146"/>
    <rect x="768" y="0" width="20" height="83"/>
  </g>
  <g class="bars-bottom-left" fill="url(#bar-up)">
    <rect x="14" y="800" width="20" height="400"/>
    <rect x="40" y="900" width="22" height="300"/>
    <rect x="73" y="972" width="18" height="228"/>
    <rect x="98" y="1052" width="20" height="148"/>
    <rect x="125" y="1115" width="20" height="85"/>
  </g>
  <g class="bars-bottom-right" fill="url(#bar-up)">
    <rect x="882" y="800" width="16" height="400"/>
    <rect x="855" y="900" width="18" height="300"/>
    <rect x="825" y="972" width="18" height="228"/>
    <rect x="797" y="1052" width="20" height="148"/>
    <rect x="772" y="1115" width="20" height="85"/>
  </g>

  <!-- illustration area -->
  <ellipse class="mouth-art" role="img" aria-label="Line illustration of a mouth biting its lip, drawn in pink outline"
           cx="311" cy="155" rx="140" ry="70" transform="rotate(12 311 155)" fill="url(#mouth-tone)"/>

  <!-- sweeping curve -->
  <path class="sweep" d="M558 255 C700 380 840 540 810 640 C770 760 500 900 172 1085"/>

  <text class="side-title" x="606" y="270" transform="rotate(50 606 270)">Quiet PLEASE</text>
  <text class="headline" x="252" y="872" transform="rotate(-29 252 872)">QUIET PLEASE</text>
  <text class="tagline" x="316" y="995" transform="rotate(-32 316 995)">Mind at work</text>
</svg>
</body>
</html>
```